Business Card Design Project - Sports Brand

Lumora is a e-commerce fitness wear brand for ladies who are into gym, pole and swim.

Card should not be overly cluttered and should include the following:

1. logo
2. Name of the company (Use "Lumora Wear Pte Ltd" for now)
3. Address of company (Use a mock address)
4. Representative's name and contact info etc. (use a mock name and contact info)
5. website address

Target Market(s)

Women who are into pole , gym, and swim.

Women who shop online

Industry/Entity Type

E-Commerce

Colors

Designer to choose colors to be used in the design.

Requirements
Nice to have
• feminine sublimation of colours

Need not be printed on traditional paper. We would like the design to be revolutionary and interesting to the eye :)
Should not have
• the design should not be traditional looking. Do not include illustrations of Bikinis, yoga poses etc. in the card.

```html
<!DOCTYPE html>
<html lang="en">
<head>
<meta charset="utf-8">
<title>Lumora Wear – Business Card</title>
<link rel="stylesheet" href="https://fonts.googleapis.com/css2?family=Encode+Sans+Condensed:wght@400;600&family=Cormorant+Garamond:wght@500&display=swap">
<style>
  :root {
    --page-bg: #ece8e6;
    --brand-red: #e03a3c;
    --brand-red-deep: #c8262f;
    --brand-pink: #e2507a;
    --splash-orange: #ee4a2e;
    --splash-pink: #e77bb0;
    --logo-wine: #a51d38;
    --band-light: #fbeef3;
    --band-pink: #e48bb3;
    --tag-grey: #555058;
    --card-white: #ffffff;
    --contact-red: #d9322b;
    --text-white: #ffffff;
  }
  * { box-sizing: border-box; margin: 0; padding: 0; }
  html, body { width: 1200px; height: 1000px; overflow: hidden; }
  body {
    background: var(--page-bg);
    font-family: "Encode Sans Condensed", "Arial Narrow", sans-serif;
    position: relative;
  }
  .card {
    position: absolute;
    left: 220px;
    width: 760px;
    height: 434px;
    overflow: hidden;
    box-shadow: 0 12px 30px rgba(60, 30, 30, 0.25);
  }
  .card--front { top: 36px; background: radial-gradient(ellipse at 45% 40%, var(--brand-pink) 0%, var(--brand-red) 70%); }
  .card--back { top: 530px; background: var(--card-white); }

  .splash {
    position: absolute;
    border-radius: 50%;
    background: linear-gradient(180deg, var(--splash-orange) 0%, #ea5a5c 45%, var(--splash-pink) 100%);
    filter: blur(1.5px);
  }
  .card--front .splash { left: 165px; top: 45px; width: 270px; height: 270px;
    background: radial-gradient(circle at 55% 60%, var(--splash-orange) 0%, #e8607e 55%, var(--splash-pink) 100%); }

  .brand-name {
    position: absolute;
    font-family: "Encode Sans Condensed", "Arial Narrow", sans-serif;
    font-weight: 600;
    color: var(--logo-wine);
    line-height: 1;
  }
  .card--front .brand-name { left: 250px; top: 170px; font-size: 110px; }

  .tag-band {
    position: absolute;
    left: 0; right: 0; top: 338px; height: 34px;
    background: linear-gradient(90deg, var(--band-pink) 0%, var(--band-light) 30%, var(--band-light) 80%, var(--band-pink) 100%);
    border-top: 2px solid #b9355a;
    border-bottom: 2px solid #b9355a;
  }
  .tagline {
    position: absolute; right: 70px; top: 2px;
    font-family: "Cormorant Garamond", Georgia, serif;
    font-size: 25px; color: var(--tag-grey); letter-spacing: 1px;
  }

  .back-strip { position: absolute; left: 0; top: 0; bottom: 0; width: 60px;
    background: linear-gradient(90deg, var(--brand-red-deep), var(--brand-red)); box-shadow: 4px 0 8px rgba(0,0,0,0.25); }
  .back-left { position: absolute; left: 60px; top: 0; bottom: 0; width: 270px; box-shadow: 5px 0 10px rgba(0,0,0,0.18); }
  .back-left .splash { left: 12px; top: 48px; width: 165px; height: 165px; }
  .back-left .brand-name { left: 90px; top: 108px; font-size: 48px; }
  .back-left .tagline-small {
    position: absolute; left: 118px; top: 160px;
    font-family: "Cormorant Garamond", Georgia, serif; font-size: 16px; color: var(--tag-grey);
  }
  .company-info { position: absolute; left: 78px; top: 300px; color: var(--contact-red); font-size: 15px; line-height: 2.3; }

  .back-right { position: absolute; left: 330px; top: 0; right: 0; bottom: 0; }
  .back-right .splash { left: 20px; top: 78px; width: 420px; height: 400px; }
  .rep { position: absolute; left: 108px; top: 162px; color: var(--text-white); }
  .rep-name { font-size: 32px; font-weight: 600; border-bottom: 2px solid var(--text-white); display: inline-block; line-height: 1.15; }
  .rep-title { font-size: 22px; font-style: italic; border-bottom: 1px solid var(--text-white); display: block; width: 190px; line-height: 1.2; }
  .rep-contact { margin-top: 30px; font-size: 15px; line-height: 1.6; }
</style>
</head>
<body>
  <section class="card card--front">
    <div class="splash" role="img" aria-label="Watercolour splash in orange red and pink"></div>
    <div class="brand-name">Lumora</div>
    <div class="tag-band"><span class="tagline">Yoga • Swim • Pole</span></div>
  </section>

  <section class="card card--back">
    <div class="back-strip"></div>
    <div class="back-left">
      <div class="splash" role="img" aria-label="Small watercolour splash in red and pink"></div>
      <div class="brand-name">Lumora</div>
      <div class="tagline-small">Yoga • Swim • Pole</div>
      <div class="company-info">
        <p>Lumora Wear Pte Ltd</p>
        <p>14 Harbourlight Ave.</p>
        <p>www.lumorawear.com</p>
      </div>
    </div>
    <div class="back-right">
      <div class="splash" role="img" aria-label="Large watercolour splash in orange red fading to pink"></div>
      <div class="rep">
        <div class="rep-name">Name Surname</div>
        <span class="rep-title">sales representative</span>
        <div class="rep-contact">
          <p>tel.: xx xx xxx xxx</p>
          <p>email: NSurname@lumorawear.com</p>
        </div>
      </div>
    </div>
  </section>
</body>
</html>
```